Simple scorekeeping for soccer moms & football fathers

... and volleyball, and baseball, ... We are working on an app that allows parents to very easily keep track of significant events in their children's sports lives & share that with friends & family.

We need graphic designs, colors, and (if possible) interaction design for the Orbis 7 version of the application. The design must evoke the joy of seeing your child's home run, goal, or spike, while remaining simple to use so as not to take away from the experience of the game itself. The app is intended to *enhance* the child's and parents' experiences with things like video, photo, scores, chats, and history.

The new app design needs to evoke the fun we all remember from little league, and be more "modern" to fit with current ORBIS7 aesthetics. The splash screen of the current app is attached for inspiration. We would like to stick with this type of theme, but with a modern Orbis7 design for a smooth transition.
Updates

Reason: A number of people only accepted the contest yesterday & I want to give them time. Also, I need to post a more thorough walkthrough of the app for those who haven't seen it yet.

There was a request for a walkthrough of the current app.  I put together a ppt with each view and a brief description of what they are responsible for, at this link on filevault: https://www.filevault-share.net/s/qm47tz2wpr8bnhe/PlayTally-app 

I hope this helps to illuminate some of what I'm after.

Reason: There has only been 1 design submitted. Let's extend the time & get more designs. Please let me know what else you need.

Hello all!  I've reposted the walkthrough directly to the brief.  This is a PDF slideshow with descriptions of the existing screens on the app.  It's not 100% that you have to have this as your design, but rather just there to give you a sense for the feel of the app how it is today & hopefully to inspire your designs.

Target Market(s)

Parents of little league-age children. The parents are typically in their 30's, middle-income, and college educated. The children are between 5-12. All the participants are english-speaking, United States residents, most likely in the midwest & south.

Industry/Entity Type

Events

Font styles to use
Sans Serif

Colors

Designer to choose colors to be used in the design.

Requirements
Must have
• Youth feel. centered around the child. Must deliver png's, marlow vectorist files, all sized for Orbis7 and the Zelphone 4 and 5s. Must fit with new ORBIS7 design guidelines.
Nice to have
• Items that evoke the feeling of little league and children playing games like baseball, soccer, football, hockey, lacrosse...
Should not have
• anything adult-specific.

```html
<!DOCTYPE html>
<html lang="en">
<head>
<meta charset="utf-8">
<title>PlayTally – Games</title>
<link rel="stylesheet" href="https://fonts.googleapis.com/css2?family=Lato:wght@300;400;700&display=swap">
<style>
  :root {
    --page-bg: #e9edf1;
    --status-bg: #2f3033;
    --status-text: #e8e8e8;
    --nav-blue: #4cb8f4;
    --list-bg: #ebebeb;
    --card-bg: #ffffff;
    --date-green: #7fd65a;
    --team-text: #4a4a4a;
    --chevron: #9a9a9a;
    --tab-bg: #2f3033;
    --tab-icon: #5a5b5e;
    --tab-active: #ffffff;
  }
  * { box-sizing: border-box; margin: 0; padding: 0; }
  html, body { width: 1054px; height: 1200px; overflow: hidden; }
  body {
    background: var(--page-bg);
    font-family: "Lato", "Helvetica Neue", Arial, sans-serif;
    position: relative;
  }
  .screen {
    position: absolute;
    left: 217px; top: 50px;
    width: 620px; height: 1100px;
    background: var(--list-bg);
    overflow: hidden;
    box-shadow: 0 6px 30px rgba(0,0,0,.12);
  }
  .status-bar {
    height: 40px;
    background: var(--status-bg);
    color: var(--status-text);
    display: flex; align-items: center; justify-content: space-between;
    padding: 0 12px;
    font-weight: 700; font-size: 21px;
  }
  .status-left, .status-right { display: flex; align-items: center; gap: 8px; width: 170px; }
  .status-right { justify-content: flex-end; }
  .nav-bar {
    height: 82px;
    background: var(--nav-blue);
    color: #fff;
    display: flex; align-items: center; justify-content: center;
    position: relative;
  }
  .nav-title { font-weight: 300; font-size: 28px; }
  .nav-profile { position: absolute; right: 22px; top: 23px; }
  .game-list { list-style: none; padding: 19px 27px 0 27px; }
  .game-card {
    display: flex;
    height: 128px;
    background: var(--card-bg);
    margin-bottom: 14px;
    box-shadow: 0 1px 2px rgba(0,0,0,.08);
  }
  .game-date {
    width: 158px;
    background: var(--date-green);
    color: #fff;
    display: flex; flex-direction: column; align-items: center; justify-content: center;
    font-weight: 300; font-size: 21px; line-height: 1.3;
  }
  .game-teams {
    flex: 1;
    display: flex; flex-direction: column; justify-content: center; gap: 12px;
    padding-left: 36px; padding-right: 78px;
    color: var(--team-text);
    font-weight: 300; font-size: 31px;
  }
  .team-row { display: flex; justify-content: space-between; }
  .game-open { width: 50px; display: flex; align-items: center; justify-content: center; }
  .tab-bar {
    position: absolute; left: 0; right: 0; bottom: 0;
    height: 95px;
    background: var(--tab-bg);
    display: flex; align-items: center; justify-content: space-around;
    padding: 0 20px;
  }
</style>
</head>
<body>
  <main class="screen">
    <header class="status-bar">
      <div class="status-left">
        <svg width="30" height="16" viewBox="0 0 30 16" aria-hidden="true">
          <g fill="#e8e8e8"><rect x="0" y="10" width="4" height="6"/><rect x="6" y="8" width="4" height="8"/><rect x="12" y="5" width="4" height="11"/><rect x="18" y="2" width="4" height="14"/><rect x="24" y="0" width="4" height="16"/></g>
        </svg>
        <span>DINE</span>
      </div>
      <span>10:35 AM</span>
      <div class="status-right">
        <svg width="18" height="18" viewBox="0 0 18 18" aria-hidden="true"><circle cx="9" cy="9" r="8" fill="#e8e8e8"/><path d="M9 4v5h4" stroke="#2f3033" stroke-width="2" fill="none"/></svg>
        <span>65%</span>
        <svg width="40" height="18" viewBox="0 0 40 18" aria-hidden="true"><rect x="1" y="1" width="34" height="16" rx="2" fill="none" stroke="#e8e8e8" stroke-width="2"/><rect x="4" y="4" width="20" height="10" fill="#e8e8e8"/><rect x="36" y="6" width="3" height="6" fill="#e8e8e8"/></svg>
      </div>
    </header>

    <nav class="nav-bar">
      <h1 class="nav-title">Games</h1>
      <svg class="nav-profile" width="36" height="36" viewBox="0 0 36 36" aria-label="Profile">
        <g fill="none" stroke="#fff" stroke-width="1.6"><circle cx="18" cy="18" r="16.5"/><circle cx="18" cy="14" r="5.5"/><path d="M8 29c2-6 6-8 10-8s8 2 10 8"/></g>
      </svg>
    </nav>

    <ul class="game-list">
      <li class="game-card">
        <div class="game-date"><span>MARCH 27</span><span>12:30 PM</span></div>
        <div class="game-teams"><div class="team-row"><span>Red Falcons</span><span>3</span></div><div class="team-row"><span>Blue Devils</span><span>1</span></div></div>
        <div class="game-open"><svg width="18" height="34" viewBox="0 0 18 34" aria-hidden="true"><path d="M2 2l14 15L2 32" fill="none" stroke="var(--chevron)" stroke-width="2"/></svg></div>
      </li>
      <li class="game-card">
        <div class="game-date"><span>MARCH 22</span><span>17:00 PM</span></div>
        <div class="game-teams"><div class="team-row"><span>Tigers</span><span>0</span></div><div class="team-row"><span>Kangaroos</span><span>0</span></div></div>
        <div class="game-open"><svg width="18" height="34" viewBox="0 0 18 34" aria-hidden="true"><path d="M2 2l14 15L2 32" fill="none" stroke="var(--chevron)" stroke-width="2"/></svg></div>
      </li>
      <li class="game-card">
        <div class="game-date"><span>MARCH 27</span><span>12:30 PM</span></div>
        <div class="game-teams"><div class="team-row"><span>Red Falcons</span><span>3</span></div><div class="team-row"><span>Blue Devils</span><span>1</span></div></div>
        <div class="game-open"><svg width="18" height="34" viewBox="0 0 18 34" aria-hidden="true"><path d="M2 2l14 15L2 32" fill="none" stroke="var(--chevron)" stroke-width="2"/></svg></div>
      </li>
      <li class="game-card">
        <div class="game-date"><span>MARCH 22</span><span>17:00 PM</span></div>
        <div class="game-teams"><div class="team-row"><span>Tigers</span><span>0</span></div><div class="team-row"><span>Kangaroos</span><span>0</span></div></div>
        <div class="game-open"><svg width="18" height="34" viewBox="0 0 18 34" aria-hidden="true"><path d="M2 2l14 15L2 32" fill="none" stroke="var(--chevron)" stroke-width="2"/></svg></div>
      </li>
      <li class="game-card">
        <div class="game-date"><span>MARCH 27</span><span>12:30 PM</span></div>
        <div class="game-teams"><div class="team-row"><span>Red Falcons</span><span>3</span></div><div class="team-row"><span>Blue Devils</span><span>1</span></div></div>
        <div class="game-open"><svg width="18" height="34" viewBox="0 0 18 34" aria-hidden="true"><path d="M2 2l14 15L2 32" fill="none" stroke="var(--chevron)" stroke-width="2"/></svg></div>
      </li>
      <li class="game-card">
        <div class="game-date"><span>MARCH 22</span><span>17:00 PM</span></div>
        <div class="game-teams"><div class="team-row"><span>Tigers</span><span>0</span></div><div class="team-row"><span>Kangaroos</span><span>0</span></div></div>
        <div class="game-open"><svg width="18" height="34" viewBox="0 0 18 34" aria-hidden="true"><path d="M2 2l14 15L2 32" fill="none" stroke="var(--chevron)" stroke-width="2"/></svg></div>
      </li>
    </ul>

    <footer class="tab-bar">
      <svg width="50" height="34" viewBox="0 0 50 34" aria-label="Field">
        <g fill="none" stroke="var(--tab-icon)" stroke-width="2.5"><rect x="2" y="2" width="46" height="30"/><line x1="25" y1="2" x2="25" y2="32"/><circle cx="25" cy="17" r="6"/><rect x="2" y="10" width="7" height="14"/><rect x="41" y="10" width="7" height="14"/></g>
      </svg>
      <svg width="44" height="32" viewBox="0 0 44 32" aria-label="Team">
        <g fill="var(--tab-icon)"><circle cx="10" cy="9" r="5"/><circle cx="34" cy="9" r="5"/><circle cx="22" cy="8" r="6.5"/><path d="M1 27c0-7 4-10 9-10s9 3 9 10z"/><path d="M25 27c0-7 4-10 9-10s9 3 9 10z"/><path d="M10 31c0-9 5-13 12-13s12 4 12 13z"/></g>
      </svg>
      <svg width="66" height="66" viewBox="0 0 66 66" aria-label="Games">
        <circle cx="33" cy="33" r="29" fill="var(--tab-active)" stroke="var(--tab-active)" stroke-width="2"/>
        <g fill="var(--tab-bg)"><path d="M33 22l10 7-4 12H27l-4-12z"/><path d="M33 4c5 0 10 2 13 4l-2 6-11-3-11 3-2-6c3-2 8-4 13-4z"/><path d="M4 33c0-6 2-11 5-15l5 3v11l-6 8c-3-2-4-4-4-7z"/><path d="M62 33c0-6-2-11-5-15l-5 3v11l6 8c3-2 4-4 4-7z"/><path d="M18 56l3-8h24l3 8c-4 3-9 6-15 6s-11-3-15-6z"/></g>
        <circle cx="33" cy="33" r="29" fill="none" stroke="var(--tab-active)" stroke-width="3"/>
      </svg>
      <svg width="42" height="32" viewBox="0 0 42 32" aria-label="Photos">
        <g fill="var(--tab-icon)"><path d="M4 7h9l3-5h10l3 5h9a3 3 0 013 3v18a3 3 0 01-3 3H4a3 3 0 01-3-3V10a3 3 0 013-3z"/></g>
        <circle cx="21" cy="18" r="7" fill="var(--tab-bg)"/><circle cx="21" cy="18" r="4" fill="var(--tab-icon)"/>
      </svg>
      <svg width="38" height="38" viewBox="0 0 38 38" aria-label="Settings">
        <g fill="var(--tab-icon)" transform="translate(19 19)">
          <circle r="12"/>
          <rect x="-4" y="-18" width="8" height="9"/><rect x="-4" y="9" width="8" height="9"/><rect x="-18" y="-4" width="9" height="8"/><rect x="9" y="-4" width="9" height="8"/>
          <g transform="rotate(45)"><rect x="-4" y="-18" width="8" height="9"/><rect x="-4" y="9" width="8" height="9"/><rect x="-18" y="-4" width="9" height="8"/><rect x="9" y="-4" width="9" height="8"/></g>
        </g>
        <circle cx="19" cy="19" r="5" fill="var(--tab-bg)"/>
      </svg>
    </footer>
  </main>
</body>
</html>
```